Stylish High End Wedding Videography/Films Website (BDMR)

We need a modern and high-end website look for our wedding video and films business. We films weddings all over the United Kingdom and at European destinations so need something to reflect our work. The website should be visually stunning with images and videos being the focal point as this is what our services are;

I have uploads of some items I like and the features the site needs to have. These have been taken from other websites using standout features.

We need the following pages;

1 - Homepage
2 - Films Index Page
3 - Individual Films Page
4 - Prices / Collection Page
5 - Reviews
6 - Options
7 - About
8 - Contact
9 - Blog Index
10 - Blog Page

All pages must be consistent so have a similar style.

Pages on menu:
Films
Prices
Reviews
Options
About
Contact

We require a responsive look too. Over 90% of our visitors access the website via their mobile devices.

Please use the colours from our logo to incorporate into the website.

Target Market(s)

Wedding Couples

Industry/Entity Type

Wedding Photography

Number of Pages Required

5+ page

Font styles to use
Sans Serif
Script

Requirements
Must have
• The logo must be in the centre of the menu at the top.

Social icons at the bottom of the page.

Use only two fonts including Lore which is supplied
Nice to have
• Different video for each page on the top header. This will play behind the menu.

```html
<!DOCTYPE html>
<html lang="en">
<head>
<meta charset="utf-8">
<title>BDMR – Unique Wedding Video and Photography</title>
<link rel="stylesheet" href="https://fonts.googleapis.com/css2?family=Montserrat:wght@400;500;600;700;800&display=swap">
<style>
:root{
  --gold:#b8985a;
  --gold-band:#a68f5c;
  --brown:#45393a;
  --brown-deep:#3e3431;
  --ink:#2b2626;
  --text:#3a3636;
  --muted:#7b7676;
  --light:#f6f6f6;
  --white:#ffffff;
}
*{margin:0;padding:0;box-sizing:border-box}
html,body{width:1200px;height:4201px;overflow:hidden}
body{font-family:'Montserrat',sans-serif;color:var(--text);background:var(--white);position:relative}
.abs{position:absolute}
section,header,footer{position:absolute;left:0;width:1200px}
.photo{position:absolute}

/* hero */
.hero{top:0;height:649px;overflow:hidden;background:#2c2a24}
.hero .photo{inset:0;background:
  radial-gradient(ellipse 170px 260px at 640px 420px,rgba(214,216,224,.85),rgba(170,172,185,.35) 60%,transparent 100%),
  radial-gradient(ellipse 90px 140px at 620px 170px,rgba(40,48,80,.8),transparent 100%),
  radial-gradient(ellipse 120px 300px at 520px 200px,rgba(225,230,235,.55),transparent 100%),
  radial-gradient(ellipse 90px 200px at 780px 250px,rgba(210,214,218,.45),transparent 100%),
  radial-gradient(ellipse 320px 140px at 1000px 40px,rgba(224,150,80,.75),transparent 100%),
  radial-gradient(ellipse 250px 180px at 940px 200px,rgba(120,96,60,.8),transparent 100%),
  radial-gradient(ellipse 260px 260px at 80px 420px,rgba(90,110,40,.85),transparent 100%),
  radial-gradient(ellipse 220px 180px at 1100px 330px,rgba(110,130,60,.55),transparent 100%),
  linear-gradient(180deg,#3a372f 0%,#4f4a3f 35%,#3b3a34 60%,#2a2925 100%)}
.hero .shade{position:absolute;inset:0;background:linear-gradient(90deg,rgba(0,0,0,.35),rgba(0,0,0,0) 50%,rgba(0,0,0,.15))}
.nav a{position:absolute;top:84px;font-size:13px;color:var(--white);text-decoration:none;font-weight:500}
.nav a.active{color:var(--gold)}
.nav .dot{position:absolute;top:90px;width:4px;height:4px;border-radius:50%;background:var(--white)}
.brand{position:absolute;left:500px;top:58px;width:200px;text-align:center;color:var(--white)}
.brand .mark{display:block;width:14px;height:14px;margin:0 auto 10px;border:2px solid var(--gold)}
.brand .name{font-size:18px;font-weight:600;letter-spacing:5px}
.hero h1{position:absolute;left:150px;top:272px;font-size:52px;font-weight:700;color:transparent;-webkit-text-stroke:1.5px var(--white);letter-spacing:1px}
.hero h2{position:absolute;left:154px;top:339px;font-size:27px;font-weight:700;color:var(--white)}
.link-more{position:absolute;font-size:11px;font-weight:700;letter-spacing:2.5px;padding-left:16px;border-left:2px solid var(--gold);line-height:16px}
.hero .link-more{left:152px;top:478px;color:var(--white)}
.counter{position:absolute;left:1092px;top:314px;color:var(--white);font-weight:700;font-size:21px}
.counter small{font-size:10px;font-weight:600}

/* services */
.services{top:649px;height:961px;background:var(--light)}
.section-title{position:absolute;font-size:28px;font-weight:700;color:var(--ink)}
.card{position:absolute;background:var(--brown);padding:62px 38px 0;color:#e9e4e1}
.card h3{font-size:18px;line-height:21px;color:var(--gold);font-weight:700}
.card p{font-size:12px;line-height:20px;margin-top:16px;color:#d9d2cf}
.card .link-more{position:static;display:inline-block;margin-top:22px;color:var(--white)}
.ph-ring{background:
  radial-gradient(circle 60px at 220px 250px,rgba(210,205,215,.7),transparent 100%),
  radial-gradient(ellipse 140px 90px at 120px 60px,rgba(230,200,205,.8),transparent 100%),
  radial-gradient(ellipse 200px 160px at 160px 300px,rgba(120,110,60,.9),transparent 100%),
  linear-gradient(160deg,#c9b8a6 0%,#8e8158 45%,#5f5836 100%)}
.ph-confetti{background:
  radial-gradient(ellipse 80px 160px at 250px 230px,rgba(235,228,214,.9),transparent 100%),
  radial-gradient(ellipse 70px 90px at 110px 150px,rgba(120,80,50,.9),transparent 100%),
  radial-gradient(ellipse 120px 80px at 60px 40px,rgba(120,130,80,.8),transparent 100%),
  linear-gradient(135deg,#6d5d48 0%,#a38b6f 45%,#cbbda6 75%,#9c8264 100%)}
.ph-sea{background:
  radial-gradient(ellipse 90px 150px at 210px 260px,rgba(240,238,234,.9),transparent 100%),
  radial-gradient(ellipse 70px 90px at 150px 90px,rgba(150,110,90,.8),transparent 100%),
  linear-gradient(180deg,#7d8589 0%,#5d6467 45%,#4c5256 70%,#3f4446 100%)}

/* experience */
.experience{top:1610px;height:459px;overflow:hidden;background:
  radial-gradient(ellipse 500px 120px at 700px 440px,rgba(70,85,45,.85),transparent 100%),
  radial-gradient(ellipse 120px 200px at 1000px 230px,rgba(30,28,26,.7),transparent 100%),
  radial-gradient(ellipse 40px 80px at 540px 340px,rgba(220,220,215,.5),transparent 100%),
  linear-gradient(180deg,#4a4a4a 0%,#464646 55%,#3b3d35 80%,#2e3028 100%)}
.big-num{position:absolute;left:98px;top:52px;font-size:380px;font-weight:700;letter-spacing:-28px;color:rgba(160,160,160,.8);line-height:.78}
.experience h3{position:absolute;left:268px;top:197px;font-size:27px;line-height:32px;color:var(--white);font-weight:700}
.experience .lead{position:absolute;left:601px;top:100px;width:446px;font-size:18px;line-height:26px;color:var(--white);text-align:justify}
.lead em{font-style:normal;color:var(--gold);font-weight:600}
.experience .body{position:absolute;left:601px;top:198px;width:446px;font-size:11.5px;line-height:20px;color:#dcdcdc;text-align:justify}
.experience .link-more{left:601px;top:338px;color:var(--white)}

/* projects */
.projects{top:2069px;height:710px;background:var(--white)}
.projects .feature{left:267px;top:174px;width:665px;height:433px;box-shadow:0 25px 50px rgba(0,0,0,.14);background:
  radial-gradient(ellipse 120px 220px at 270px 290px,rgba(235,232,228,.85),transparent 100%),
  radial-gradient(ellipse 60px 60px at 240px 310px,rgba(170,40,40,.7),transparent 100%),
  radial-gradient(ellipse 130px 240px at 380px 260px,rgba(20,18,18,.9),transparent 100%),
  radial-gradient(ellipse 90px 120px at 120px 120px,rgba(110,90,70,.6),transparent 100%),
  radial-gradient(ellipse 150px 120px at 560px 80px,rgba(130,140,110,.55),transparent 100%),
  linear-gradient(135deg,#3e3833 0%,#6a6058 45%,#2e2a28 100%)}
.play{position:absolute;left:290px;top:174px;width:86px;height:86px;border-radius:50%;background:rgba(80,80,80,.55)}
.vertical-label{position:absolute;left:195px;top:607px;transform:rotate(-90deg);transform-origin:0 0;font-size:18px;font-weight:700;color:var(--ink);white-space:nowrap}
.vertical-label span{color:var(--gold)}
.num-outline{position:absolute;font-size:50px;font-weight:700;color:transparent;-webkit-text-stroke:1.5px var(--gold)}
.num-solid{position:absolute;font-size:50px;font-weight:800;color:var(--gold)}

/* testimonial */
.testimonial{top:2779px;height:396px;background:var(--light);text-align:center}
.testimonial blockquote{position:absolute;left:240px;top:82px;width:720px;font-size:19px;line-height:31px;color:#6b6767}
.testimonial sup{color:var(--gold);font-size:12px}
.avatar{position:absolute;left:570px;top:236px;width:60px;height:60px;border-radius:50%;background:radial-gradient(circle at 40% 40%,#c9b7a4,#6e5e50 70%,#3e342e)}
.testimonial .who{position:absolute;left:0;width:1200px;top:308px;font-size:14px;font-weight:700;color:var(--ink)}

/* photography */
.photography{top:3175px;height:618px;background:var(--white)}
.album{position:absolute;top:152px;width:282px}
.album .thumb{width:282px;height:282px}
.album h4{margin-top:28px;font-size:18px;font-weight:700;color:var(--ink)}
.album.active h4{color:var(--gold)}
.album p{margin-top:10px;font-size:12px;line-height:20px;color:var(--muted)}
.th-1{background:
  radial-gradient(ellipse 90px 110px at 120px 220px,rgba(245,243,238,.95),transparent 100%),
  radial-gradient(ellipse 70px 80px at 110px 80px,rgba(220,200,150,.85),transparent 100%),
  radial-gradient(ellipse 80px 140px at 230px 200px,rgba(40,48,70,.9),transparent 100%),
  linear-gradient(135deg,#a39a74 0%,#c3b895 50%,#7d7a5e 100%)}
.th-2{background:
  radial-gradient(ellipse 80px 140px at 110px 170px,rgba(240,240,240,.95),transparent 100%),
  radial-gradient(ellipse 60px 160px at 230px 150px,rgba(30,30,30,.9),transparent 100%),
  linear-gradient(180deg,#8c8c8c 0%,#c8c8c8 45%,#6e6e6e 100%)}
.th-3{background:
  radial-gradient(ellipse 60px 70px at 110px 180px,rgba(90,120,80,.95),transparent 100%),
  radial-gradient(ellipse 70px 150px at 90px 200px,rgba(170,195,205,.9),transparent 100%),
  radial-gradient(ellipse 70px 150px at 200px 170px,rgba(170,170,160,.9),transparent 100%),
  linear-gradient(180deg,#d9ddd6 0%,#9aa58e 45%,#6f7f62 100%)}

/* cta */
.cta{top:3793px;height:152px;background:var(--gold-band)}
.cta h3{position:absolute;left:293px;top:58px;font-size:28px;font-weight:700;color:var(--brown-deep)}
.cta .btn{position:absolute;left:690px;top:52px;width:190px;height:48px;background:var(--brown-deep);color:var(--gold);font-size:12px;font-weight:600;letter-spacing:1px;display:flex;align-items:center;justify-content:center}

/* footer */
.site-footer{top:3945px;height:256px;background:var(--brown)}
.foot-brand{position:absolute;left:155px;top:60px;display:flex;align-items:center;gap:12px;color:var(--gold);font-size:34px;font-weight:700;letter-spacing:3px}
.foot-brand .mark{width:18px;height:18px;border:2px solid var(--gold)}
.foot-col{position:absolute;top:68px;color:var(--white)}
.foot-col h5{font-size:12px;font-weight:600;letter-spacing:3px}
.foot-col .big{margin-top:18px;font-size:19px}
.foot-col .big em{font-style:normal;color:var(--gold)}
.foot-col .small{margin-top:8px;font-size:12px;color:#d8d1ce}
.rule{position:absolute;left:78px;top:192px;width:1044px;height:1px;background:rgba(255,255,255,.15)}
.copyright{position:absolute;left:153px;top:219px;font-size:11px;color:#d8d1ce}
.social{position:absolute;top:210px;width:30px;height:30px;border-radius:50%;background:rgba(255,255,255,.14);border:1px solid rgba(255,255,255,.35)}
</style>
</head>
<body>

<header class="hero">
  <div class="photo" role="img" aria-label="Bride and groom embracing in front of a waterfall at dusk"></div>
  <div class="shade"></div>
  <nav class="nav">
    <a class="active" style="left:228px">Films</a>
    <span class="dot" style="left:280px"></span>
    <a style="left:303px">Prices</a>
    <span class="dot" style="left:361px"></span>
    <a style="left:383px">Reviews</a>
    <a style="left:764px">Options</a>
    <span class="dot" style="left:834px"></span>
    <a style="left:856px">About</a>
    <span class="dot" style="left:916px"></span>
    <a style="left:939px">Contact</a>
  </nav>
  <div class="brand"><span class="mark"></span><span class="name">BDMR</span></div>
  <h1>Unique Wedding</h1>
  <h2>Video and Photography</h2>
  <span class="link-more">WATCH VIDEO</span>
  <svg class="abs" style="left:1116px;top:270px" width="18" height="12" viewBox="0 0 18 12"><path d="M2 10 9 3l7 7" fill="none" stroke="#fff" stroke-width="1.5"/></svg>
  <div class="counter">01<small> / 06</small></div>
  <svg class="abs" style="left:1116px;top:364px" width="18" height="12" viewBox="0 0 18 12"><path d="M2 2l7 7 7-7" fill="none" stroke="#fff" stroke-width="1.5"/></svg>
</header>

<section class="services">
  <h2 class="section-title" style="left:153px;top:138px">What Can We Do</h2>
  <div class="photo ph-ring" style="left:600px;top:122px;width:332px;height:360px" role="img" aria-label="Close-up of an engagement ring hanging from a blossom branch"></div>
  <div class="photo ph-confetti" style="left:267px;top:252px;width:333px;height:357px" role="img" aria-label="Laughing couple under falling confetti"></div>
  <div class="photo ph-sea" style="left:600px;top:482px;width:332px;height:356px" role="img" aria-label="Groom kissing bride by the sea"></div>
  <div class="card" style="left:536px;top:58px;width:282px;height:281px">
    <h3>Creative<br>Conceptions</h3>
    <p>Sed do eiusmod tempor<br>incididunt ut labore<br>dolore magna ...</p>
    <span class="link-more">MORE</span>
  </div>
  <div class="card" style="left:230px;top:420px;width:230px;height:228px;padding-top:50px">
    <h3>Shooting &amp;<br>Editing</h3>
    <p>Sed do eiusmod tempor<br>incididunt ut labore<br>dolore magna ...</p>
    <span class="link-more">MORE</span>
  </div>
  <div class="card" style="left:562px;top:648px;width:229px;height:229px;padding-top:50px">
    <h3>Unique<br>Photography</h3>
    <p>Sed do eiusmod tempor<br>incididunt ut labore<br>dolore magna ...</p>
    <span class="link-more">MORE</span>
  </div>
</section>

<section class="experience">
  <div class="photo" style="inset:0" role="img" aria-label="Videographer filming a couple in a field under a stormy sky"></div>
  <div class="big-num">13</div>
  <h3>Years of Successful<br>experience</h3>
  <p class="lead">Sed ut perspiciatis <em>unde omnis iste natus</em> error sit voluptatem doloremque laudantium, <em>ipsa quae ab illo inventore</em> veritatis et quasi</p>
  <p class="body">Nemo enim ipsam voluptatem quia voluptas sit aspernatur aut odit aut fugit, sed quia consequuntur magni dolores eos qui ratione voluptatem sequi nesciunt. Neque porro quisquam est, qui dolorem ipsum quia dolor sit amet, consectetur, adipisci velit, sed quia non numquam eius modi tempora incidunt ut labore et dolore magnam</p>
  <span class="link-more">ABOUT US</span>
</section>

<section class="projects">
  <h2 class="section-title" style="left:150px;top:86px">Latest Projects</h2>
  <svg class="abs" style="left:202px;top:170px" width="12" height="20" viewBox="0 0 12 20"><path d="M10 2 2 10l8 8" fill="none" stroke="#cfcfcf" stroke-width="1.5"/></svg>
  <div class="photo feature" role="img" aria-label="Couple walking through a shower of confetti with guests">
    <div class="play"><svg width="86" height="86" viewBox="0 0 86 86"><path d="M36 28v30l24-15z" fill="none" stroke="#fff" stroke-width="2.5"/></svg></div>
  </div>
  <div class="num-outline" style="left:258px;top:150px">2</div>
  <div class="num-solid" style="left:908px;top:580px">4</div>
  <div class="vertical-label"><span>03.</span> Ella &amp; Tom Harrow</div>
  <svg class="abs" style="left:982px;top:590px" width="12" height="20" viewBox="0 0 12 20"><path d="M2 2l8 8-8 8" fill="none" stroke="#333" stroke-width="1.5"/></svg>
</section>

<section class="testimonial">
  <blockquote><sup>“</sup> Sed ut perspiciatis unde omnis iste natus error sit voluptatem<br>accusantium doloremque laudantium, totam rem aperiam, eaque ipsa<br>quae ab illo inventore veritatis et quasi architecto<br>beatae vitae dicta sunt explicabo <sup>”</sup></blockquote>
  <div class="avatar" role="img" aria-label="Portrait of the reviewing couple"></div>
  <div class="who">Nora Whitfield</div>
</section>

<section class="photography">
  <h2 class="section-title" style="left:150px;top:88px">Photography</h2>
  <svg class="abs" style="left:71px;top:284px" width="12" height="20" viewBox="0 0 12 20"><path d="M10 2 2 10l8 8" fill="none" stroke="#cfcfcf" stroke-width="1.5"/></svg>
  <div class="album active" style="left:153px">
    <div class="thumb th-1" role="img" aria-label="Smiling bride and groom portrait outdoors"></div>
    <h4>Mia &amp; Leo</h4>
    <p>Lorem Ipsum is simply dummy text<br>printing and typesettin</p>
  </div>
  <div class="album" style="left:458px">
    <div class="thumb th-2" role="img" aria-label="Black and white photo of couple running through smoke"></div>
    <h4>Ella &amp; Tom</h4>
    <p>Lorem Ipsum is simply dummy text<br>printing and typesettin</p>
  </div>
  <div class="album" style="left:763px">
    <div class="thumb th-3" role="img" aria-label="Couple embracing in green hills with a bouquet"></div>
    <h4>Mia &amp; Leo</h4>
    <p>Lorem Ipsum is simply dummy text<br>printing and typesettin</p>
  </div>
  <svg class="abs" style="left:1116px;top:284px" width="12" height="20" viewBox="0 0 12 20"><path d="M2 2l8 8-8 8" fill="none" stroke="#333" stroke-width="1.5"/></svg>
</section>

<section class="cta">
  <h3>Start your project with us</h3>
  <span class="btn">Get Started Now!</span>
</section>

<footer class="site-footer">
  <div class="foot-brand"><span class="mark"></span>BDMR</div>
  <div class="foot-col" style="left:352px">
    <h5>CONTACT US</h5>
    <div class="big">Call. <em>+1 800 555 0142</em></div>
    <div class="small">e. info@bdmr-films.com</div>
  </div>
  <div class="foot-col" style="left:647px">
    <h5>GET IN TOUCH</h5>
    <div class="big">Studio 14 Alder Lane,</div>
    <div class="small">Mill Row, Leeds 20417</div>
  </div>
  <svg class="abs" style="left:1026px;top:72px" width="14" height="22" viewBox="0 0 14 22"><path d="M7 21V2M1 8l6-6 6 6" fill="none" stroke="#b8985a" stroke-width="1.5"/></svg>
  <div class="rule"></div>
  <div class="copyright">2020 © BDMR. All Rights Reserved.</div>
  <span class="social" style="left:903px" aria-label="Social link 1"></span>
  <span class="social" style="left:942px" aria-label="Social link 2"></span>
  <span class="social" style="left:979px" aria-label="Social link 3"></span>
  <span class="social" style="left:1018px" aria-label="Social link 4"></span>
</footer>

</body>
</html>
```